Darrow Consulting needs a quality & professional business card!

I am a recruitment and employment consultant from Brisbane, Australia and I had a fantastic logo organised by this community to I am hoping the business card will be the same.

I have attached the Darrow consulting logo that ideally would feature on the back of the business card. There are a number of logos for you to use as you see fit. I would like the colour cheme to match that of the Darrow Consulting logo. I also have a secondary company called Career Lantern Australia and I have included that logo as well. While it is an important part of the business I don't want this logo feature too predominantly as I am moving out of this space. This logo was created by myself and is of low quality. Feel free to use the icon and words however you want. The winning design will be smart, professional and eye-catching.

The information I am looking for in the business card is:
Name: Gavin Darrow
Position: Founder & Director
Phone: (07) 3519 6482
Mobile: 0431 586 207
Email: gavin@careerlantern.com.au

Target Market(s)

Recruiters, government, large companies

Contact Information for Business Card

Name: Gavin Darrow
Phone: (07) 3519 6482
Mobile: 0431 586 207
Web: www.careerlantern.com.au

Font styles to use
Serif
Sans Serif

Requirements
Must have
• Darrow Consulting Logo on reverse side
• Contact details on front side with smaller reference to Darrow Consulting logo and Career Lantern Australia logo

```html
<!DOCTYPE html>
<html lang="en">
<head>
<meta charset="utf-8">
<title>Gavin Darrow – Business Card</title>
<link rel="stylesheet" href="https://fonts.googleapis.com/css2?family=Lato:wght@400;700&family=Merriweather:wght@700&display=swap">
<style>
  :root {
    --backdrop: #3a3d40;
    --card: #ffffff;
    --ink: #1d1d1d;
    --ink-soft: #333333;
    --band: #0b9bcb;
    --band-text: #ffffff;
  }
  * { box-sizing: border-box; margin: 0; padding: 0; }
  html, body {
    width: 1200px; height: 1141px; overflow: hidden;
    background: var(--backdrop);
    font-family: "Lato", Arial, sans-serif;
    color: var(--ink);
  }
  .card {
    position: absolute; left: 232px; width: 730px; height: 414px;
    background: var(--card); border-radius: 30px; overflow: hidden;
  }
  .card--front { top: 120px; }
  .card--back { top: 570px; }

  .brand { position: absolute; display: flex; align-items: center; gap: 18px; }
  .brand__mark { width: 64px; height: 64px; border-radius: 50%; background: var(--ink); flex: none; }
  .brand__name {
    font-family: "Merriweather", Georgia, serif; font-weight: 700;
    font-size: 34px; line-height: 1.15; color: var(--ink);
  }
  .brand__name span { display: block; }
  .card--front .brand { left: 43px; top: 45px; }
  .card--back .career { left: 177px; top: 40px; }

  .band {
    position: absolute; left: 0; top: 173px; width: 100%; height: 55px;
    background: var(--band); color: var(--band-text);
    display: flex; align-items: center; padding-left: 43px;
  }
  .band__name { font-weight: 700; font-size: 28px; }
  .band__divider { width: 1px; height: 22px; background: rgba(255,255,255,.8); margin: 0 22px 0 30px; }
  .band__role { font-size: 18px; }

  .contacts { position: absolute; left: 43px; top: 270px; list-style: none; }
  .contacts li {
    display: flex; align-items: center; gap: 13px;
    font-size: 17px; color: var(--ink-soft); height: 26.5px;
  }
  .contacts svg { width: 18px; height: 18px; fill: var(--ink); flex: none; }

  .consulting { position: absolute; display: flex; align-items: center; gap: 20px; }
  .consulting__mark { width: 44px; height: 44px; background: var(--ink); flex: none; }
  .consulting__name { font-family: "Lato", Arial, sans-serif; font-weight: 400; font-size: 40px; color: var(--ink); letter-spacing: 1px; }
  .card--front .consulting { left: 330px; top: 296px; }
  .card--front .consulting__name { font-size: 32px; }
  .card--back .consulting { left: 190px; top: 222px; }

  .web { position: absolute; left: 0; width: 100%; top: 352px; text-align: center; font-size: 16px; color: var(--ink); }
</style>
</head>
<body>
  <section class="card card--front">
    <div class="brand career">
      <div class="brand__mark"></div>
      <div class="brand__name"><span>Career Lantern</span><span>Australia</span></div>
    </div>

    <div class="band">
      <span class="band__name">Gavin Darrow</span>
      <span class="band__divider"></span>
      <span class="band__role">Founder &amp; Director</span>
    </div>

    <ul class="contacts">
      <li><svg viewBox="0 0 24 24" aria-hidden="true"><path d="M2 9c2-4 18-4 20 0l-1 3-4-1V8H7v3l-4 1zM6 13h12l2 7H4z"/></svg>(07) 3519 6482</li>
      <li><svg viewBox="0 0 24 24" aria-hidden="true"><path d="M6 3l3 4-2 2c1 3 4 6 7 7l2-2 4 3-2 3C10 20 4 14 3 5z"/></svg>0431 586 207</li>
      <li><svg viewBox="0 0 24 24" aria-hidden="true"><path d="M3 6h18v2l-9 6-9-6zM3 10l9 6 9-6v8H3z"/></svg>gavin@careerlantern.com.au</li>
      <li><svg viewBox="0 0 24 24" aria-hidden="true"><circle cx="12" cy="12" r="9"/><path d="M8 7c2 1 3 3 1 5s1 4 3 4M15 6c-1 2 1 3 3 4" stroke="#fff" stroke-width="1.6" fill="none"/></svg>www.careerlantern.com.au</li>
    </ul>

    <div class="consulting">
      <div class="consulting__mark"></div>
      <div class="consulting__name">Darrow Consulting</div>
    </div>
  </section>

  <section class="card card--back">
    <div class="brand career">
      <div class="brand__mark"></div>
      <div class="brand__name"><span>Career Lantern</span><span>Australia</span></div>
    </div>

    <div class="consulting">
      <div class="consulting__mark"></div>
      <div class="consulting__name">Darrow Consulting</div>
    </div>

    <p class="web">www.careerlantern.com.au</p>
  </section>
</body>
</html>
```